New Business Card Design Project

I have a logo I would like to use on the business card. I want something that will stand out and that will be remembered.

Target Market(s)

People who collect gems, minerals and crystals.

Contact Information for Business Card

email - mkthestonefalcon@vendrollo.com
phone # 917-406-2581

Font styles to use
Serif
Sans Serif
Decorative

Colors

Designer to choose colors to be used in the design.

Requirements
Must have
• The logo...two to choose from.
Nice to have
• An eye catching and memorable way to draw in people who collect gems minerals and crystals.

```html
<!DOCTYPE html>
<html lang="en">
<head>
<meta charset="utf-8">
<title>The Stone Falcon – Business Card</title>
<link href="https://fonts.googleapis.com/css2?family=Exo+2:ital,wght@0,500;0,700;0,800;1,800&display=swap" rel="stylesheet">
<style>
  :root {
    --bg: #3b3c3e;
    --card: #1d1e20;
    --white: #f2f2f2;
    --blue: #0f1fc8;
    --mark: #d9d9d9;
  }
  * { margin: 0; padding: 0; box-sizing: border-box; }
  html, body { width: 799px; height: 1200px; overflow: hidden; }
  body {
    background: var(--bg);
    font-family: "Exo 2", Arial, sans-serif;
    position: relative;
  }
  .card {
    position: absolute;
    left: 60px;
    width: 679px;
    height: 388px;
    background: var(--card);
    border-radius: 6px;
    overflow: hidden;
    box-shadow: 0 14px 30px rgba(0,0,0,.45);
  }
  .card--front { top: 150px; }
  .card--back { top: 670px; }

  .brand-mark {
    position: absolute;
    width: 120px; height: 120px;
    border-radius: 50%;
    background: var(--mark);
  }
  .card--front .brand-mark { left: 70px; top: 104px; }
  .card--back .brand-mark { left: 66px; top: 70px; width: 110px; height: 110px; }

  .brand-name {
    position: absolute;
    left: 216px; top: 128px;
    color: var(--white);
    font-weight: 800;
    font-size: 44px;
    line-height: 1;
    letter-spacing: 1px;
  }
  .rule {
    position: absolute;
    height: 3px;
    background: var(--blue);
  }
  .card--front .rule { left: 216px; top: 190px; width: 400px; }
  .tagline {
    position: absolute;
    color: var(--blue);
    font-weight: 700;
    font-size: 15px;
    letter-spacing: 5px;
  }
  .card--front .tagline { left: 216px; top: 204px; }

  .contact {
    position: absolute;
    left: 206px; top: 92px;
    color: var(--white);
  }
  .contact__phone {
    font-weight: 800;
    font-style: italic;
    font-size: 38px;
    line-height: 1;
  }
  .contact__divider {
    display: flex; align-items: center; gap: 10px;
    margin: 8px 0 6px;
  }
  .contact__divider .line { flex: 1; height: 3px; background: var(--blue); }
  .contact__name {
    color: var(--blue);
    font-weight: 800;
    font-size: 17px;
    letter-spacing: 1px;
  }
  .contact__email {
    font-weight: 700;
    font-size: 18px;
    letter-spacing: .3px;
  }
  .band {
    position: absolute;
    left: 0; bottom: 0;
    width: 679px; height: 190px;
  }
  .card--back .tagline {
    color: var(--white);
    left: 40px; bottom: 34px;
    font-size: 15px;
  }
</style>
</head>
<body>
  <section class="card card--front">
    <div class="brand-mark" aria-hidden="true"></div>
    <div class="brand-name">THE STONE FALCON</div>
    <div class="rule"></div>
    <div class="tagline">GEMS · MINERALS · CRYSTALS</div>
  </section>

  <section class="card card--back">
    <div class="brand-mark" aria-hidden="true"></div>
    <div class="contact">
      <div class="contact__phone">CALL: 917-406-2581</div>
      <div class="contact__divider">
        <span class="line"></span>
        <span class="contact__name">THE STONE FALCON</span>
        <span class="line"></span>
      </div>
      <div class="contact__email">MKTHESTONEFALCON@VENDROLLO.COM</div>
    </div>
    <svg class="band" viewBox="0 0 679 190" preserveAspectRatio="none" aria-hidden="true">
      <path d="M0 20 Q 360 -10 679 190 L 0 190 Z" fill="var(--blue)"/>
    </svg>
    <div class="tagline">GEMS · MINERALS · CRYSTALS</div>
  </section>
</body>
</html>
```